Internet Service Tech provider product flyer redesign - Skyloft Netlink

We have created the attached flyer in Word and also attached a PDF. All the content is correct. We just need a complete re-design of the flyer with new relevant hi-res images (based on content) and a more streamlined/cleaner layout.

This product is an entire in-building WIFI system for Body's Corporate in High Rise buildings.

We are a Brisbane-based internet tech company that specialises in providing solutions for High Rise buildings

Body text style - Helvetica Light

Internet

```html
<!DOCTYPE html>
<html lang="en">
<head>
<meta charset="utf-8">
<title>Skyloft Netlink – Flyer Spread</title>
<link href="https://fonts.googleapis.com/css2?family=Arimo:ital,wght@0,400;0,700;1,700&display=swap" rel="stylesheet">
<style>
  :root {
    --navy: #1e2b38;
    --slate: #4a6070;
    --row-light: #b9c8d1;
    --row-dark: #5a7080;
    --cell-light: #b8c7d0;
    --paper: #f3f4f5;
    --ink: #1f2326;
    --quote: #4b6275;
    --stage: #e4e5e7;
  }
  * { box-sizing: border-box; margin: 0; padding: 0; }
  html, body { width: 1200px; height: 1000px; overflow: hidden; background: var(--stage); }
  body { font-family: "Arimo", Arial, sans-serif; color: var(--ink); }
  .stage { position: relative; width: 1200px; height: 1000px; }

  .page {
    position: absolute; top: 90px; height: 715px; width: 536px;
    background: linear-gradient(180deg, #fafafa 0%, var(--paper) 40%, #dfe2e4 100%);
    overflow: hidden;
  }
  .page--left { left: 62px; }
  .page--right { left: 599px; }

  .hero { position: absolute; left: 0; top: 0; width: 536px; height: 212px; }
  .hero svg { display: block; }

  .hero-title {
    position: absolute; left: 0; top: 155px; width: 536px; height: 57px;
    background: rgba(45, 48, 52, 0.82);
    color: #fff; font-weight: 700; font-size: 16px; line-height: 19px;
    padding: 8px 0 0 50px;
  }
  .page--right .hero-title { top: 152px; height: 54px; text-align: right; padding: 18px 40px 0 0; }

  .stat-bar {
    position: absolute; left: 38px; top: 215px; width: 460px; height: 40px;
    background: var(--slate); border: 3px solid #a7b4bd; border-radius: 4px;
    color: #fff; font-style: italic; font-weight: 700; font-size: 16px;
    text-align: center; line-height: 34px;
  }
  .stat-bar strong { font-size: 21px; }

  .copy { position: absolute; left: 38px; width: 462px; font-size: 11px; font-weight: 400; line-height: 15.5px; }
  .copy--intro { top: 273px; }
  .copy--plan { top: 409px; }
  .quote {
    position: absolute; left: 38px; top: 363px; width: 462px; text-align: center;
    color: var(--quote); font-style: italic; font-weight: 700; font-size: 14px; line-height: 17px;
  }

  .table { position: absolute; display: grid; background: #fff; gap: 1px; }
  .table .head {
    background: var(--navy); color: #fff; font-weight: 700; text-align: center;
    display: flex; align-items: center; justify-content: center;
  }
  .table .cell { display: flex; align-items: center; justify-content: center; text-align: center; font-weight: 400; }

  .benefits { left: 38px; top: 475px; width: 460px; grid-template-columns: repeat(3, 1fr); grid-template-rows: 38px minmax(126px, auto); }
  .benefits .head { font-size: 12.5px; line-height: 15px; }
  .benefits .cell { background: var(--cell-light); font-size: 11px; line-height: 13px; text-align: left; align-items: flex-start; justify-content: flex-start; padding: 9px 10px 8px 12px; }

  .tech { left: 37px; top: 279px; width: 460px; grid-template-columns: repeat(3, 1fr); grid-template-rows: 38px repeat(7, 38px); }
  .tech .head { font-size: 13px; line-height: 15px; }
  .tech .cell { font-size: 9px; line-height: 11px; padding: 0 8px; }
  .tech .cell.light { background: var(--row-light); color: #1f2a33; }
  .tech .cell.dark { background: var(--row-dark); color: #fff; }

  .footer { position: absolute; left: 0; top: 683px; width: 536px; height: 31px; }
  .footer svg { position: absolute; inset: 0; }
  .footer .cta { position: absolute; left: 38px; top: 1px; color: #fff; font-weight: 400; font-size: 25px; line-height: 29px; }
  .footer .contact { position: absolute; right: 12px; top: 10px; color: #fff; font-size: 7.5px; font-weight: 400; white-space: nowrap; }
  .footer .contact b { font-weight: 700; }
  .footer .sep { display: inline-block; width: 1px; height: 10px; background: #fff; vertical-align: middle; margin: 0 5px; }
  .page--right .footer .contact { right: 48px; font-weight: 700; }
  .page--right .footer .sep { margin: 0 10px; }
</style>
</head>
<body>
<div class="stage">

  <section class="page page--left">
    <div class="hero">
      <svg width="536" height="212" viewBox="0 0 536 212">
        <defs>
          <linearGradient id="citySky" x1="0" y1="0" x2="0" y2="1">
            <stop offset="0" stop-color="#3a3d40"/>
            <stop offset="0.6" stop-color="#7a7d80"/>
            <stop offset="1" stop-color="#9b9ea1"/>
          </linearGradient>
        </defs>
        <polygon points="0,0 453,0 536,212 0,212" fill="url(#citySky)" role="img" aria-label="Night skyline of high-rise city towers in monochrome"/>
        <polygon points="468,0 618,0 536,200" fill="var(--slate)"/>
      </svg>
      <div class="hero-title">Why Body’s Corporate need to provide<br>Skyloft Netlink?</div>
    </div>

    <div class="stat-bar">On average, every Australian has <strong>2.6*</strong> wireless devices.</div>

    <p class="copy copy--intro">The demand and consumption of digital content and the way it is delivered to tenants, owners, guests, and consumers is increasing exponentially every day. This massive increase in digital demand means Body’s Corporate need to ensure that their buildings Communication, Internet and WIFI infrastructure is upgraded properly to cater for such mass amounts of digital demand by residents.</p>

    <p class="quote">“Internet is now considered by many as a utility,<br>just like water, gas and electricity”</p>

    <p class="copy copy--plan">We can help Body’s Corporate plan, project manage and bulk supply all aspects of upgrading and implementing a High-Rise WIFI build that is designed from the ground up for high-rise buildings.</p>

    <div class="table benefits">
      <div class="head">Meet Resident<br>Demand</div>
      <div class="head">Increase Building<br>Value</div>
      <div class="head">Fully Managed<br>Service</div>
      <div class="cell">Ensure that your building/s residents have access to proper digital connectivity, Fibre-type speed Internet, and HD WIFI using a bulk supply service that is scalable with future usage and growth</div>
      <div class="cell">Help owners/investors increase their ROI on their apartments by providing bulk high speed internet services that’s delivered through a state of the art HD WIFI system designed for your building</div>
      <div class="cell">Ensure that your building/s residents have access to proper digital connectivity, Fibre-type speed Internet, and HD WIFI using a bulk supply service that is scalable with future usage and growth</div>
    </div>

    <footer class="footer">
      <svg width="536" height="31" viewBox="0 0 536 31">
        <polygon points="0,0 536,0 536,31 0,31" fill="var(--navy)"/>
        <polygon points="205,0 536,0 536,31 190,31" fill="var(--slate)"/>
      </svg>
      <span class="cta">Get in touch</span>
      <span class="contact"><b>GPO BOX:</b> 1188 Brisbane QLD 4001<span class="sep"></span><b>Phone:</b> 1300 555 010<span class="sep"></span><b>Fax:</b> 1300 555 020</span>
    </footer>
  </section>

  <section class="page page--right">
    <div class="hero">
      <svg width="536" height="212" viewBox="0 0 536 212">
        <defs>
          <radialGradient id="techGlow" cx="0.55" cy="0.35" r="0.7">
            <stop offset="0" stop-color="#f2f3f4"/>
            <stop offset="0.5" stop-color="#a4a8ac"/>
            <stop offset="1" stop-color="#55595d"/>
          </radialGradient>
        </defs>
        <polygon points="0,0 536,0 536,212 4,212 0,200" fill="url(#techGlow)" role="img" aria-label="Close-up of a wireless access point device on a glowing technical backdrop"/>
        <polygon points="0,0 81,0 0,200" fill="var(--slate)"/>
        <polygon points="81,0 91,0 4,212 0,212 0,200" fill="#fff"/>
      </svg>
      <div class="hero-title">Our Technologies</div>
    </div>

    <div class="table tech">
      <div class="head">BULK SUPPLY</div>
      <div class="head">HD WIFI</div>
      <div class="head">AUTOMATED<br>BILLING</div>

      <div class="cell light">Licensed telecommunications and internet service carrier</div>
      <div class="cell light">High definition output up to 30+dBm</div>
      <div class="cell light">Tier 1 PCS-DSS certified</div>

      <div class="cell dark">Technology designed for multi-resident usage</div>
      <div class="cell dark">Multi-radio design</div>
      <div class="cell dark">Branded web portal for payment gateway</div>

      <div class="cell light">Corporate backup connections included</div>
      <div class="cell light">10/100/1000 Ethernet LAN connection</div>
      <div class="cell light">Fast payment processing</div>

      <div class="cell dark">Up to 1000Mbps speed downloads/uploads</div>
      <div class="cell dark">Up to 300Mbps data transfer rates – per radio</div>
      <div class="cell dark">SSL security for payment transactions</div>

      <div class="cell light">1000Mbps embedded network infrastructure</div>
      <div class="cell light">LED signal strength display</div>
      <div class="cell light">Local, friendly, and professional support</div>

      <div class="cell dark">Professional service guaranteed</div>
      <div class="cell dark">SNMP remote management and configuration</div>
      <div class="cell dark">Guest self service and payment</div>

      <div class="cell light">99.999% uptime service level agreements</div>
      <div class="cell light">Stealth design to blend into building aesthetics</div>
      <div class="cell light">Get paid 24/7</div>
    </div>

    <footer class="footer">
      <svg width="536" height="31" viewBox="0 0 536 31">
        <polygon points="0,0 536,0 536,31 0,31" fill="var(--navy)"/>
        <polygon points="215,0 536,0 536,31 200,31" fill="var(--slate)"/>
        <polygon points="203,0 211,0 196,31 188,31" fill="#dfe3e6"/>
      </svg>
      <span class="cta">Get in touch</span>
      <span class="contact">1300 555 010<span class="sep"></span>www.skyloftnetlink.com.au</span>
    </footer>
  </section>

</div>
</body>
</html>
```